Dental Office Needs Exciting New Stationary

We need a stationary design that incorporates the logo that we already have and would like to keep the existing color scheme. We need something clean and professional. This is a Endodontic (root canals) office and must represent a dental specialist's office. I need a design for a business card, envelope, and letterhead that all coordinate. I would like the business card to incorporate the information in the business card sample that I am providing. I made the business card design myself but would like to see a better one.

```html
<!DOCTYPE html>
<html lang="en">
<head>
<meta charset="utf-8">
<title>Summit Endodontics – Envelope Set</title>
<link rel="stylesheet" href="https://fonts.googleapis.com/css2?family=Montserrat:wght@300;400;700&display=swap">
<style>
  :root {
    --backdrop: #ebebeb;
    --paper: #f6f6f6;
    --paper-edge: #dcdcdc;
    --brand-blue: #1f5fb0;
    --brand-navy: #183f82;
    --brand-light: #2b7bd0;
    --band-pale: #a9c4e6;
    --band-grey: #a9a9ab;
    --ink: #3a3a3a;
    --ink-soft: #9a9a9c;
  }
  * { box-sizing: border-box; margin: 0; padding: 0; }
  html, body {
    width: 1200px; height: 795px; overflow: hidden;
    background: var(--backdrop);
    font-family: "Montserrat", sans-serif;
  }
  .canvas { position: relative; width: 1200px; height: 795px; }

  .envelope {
    position: absolute;
    width: 640px; height: 290px;
    background: var(--paper);
    box-shadow: 0 2px 0 var(--paper-edge), 0 14px 30px rgba(0,0,0,.12);
    overflow: hidden;
  }

  /* back of envelope */
  .envelope--back { left: 60px; top: 60px; }
  .envelope__flap {
    position: absolute; left: 0; top: 0; width: 100%; height: 96px;
    background: linear-gradient(90deg, var(--brand-navy) 0%, var(--brand-light) 50%, var(--brand-navy) 100%);
    border-bottom-left-radius: 18px;
    border-bottom-right-radius: 18px;
  }
  .envelope__flap-mark {
    position: absolute; left: 50%; top: 48px; transform: translate(-50%, -50%);
    width: 40px; height: 40px; border-radius: 50%;
    background: rgba(255,255,255,.12);
  }

  /* front of envelope */
  .envelope--front { left: 500px; top: 440px; }
  .brand {
    position: absolute; left: 40px; top: 34px;
    display: flex; align-items: center; gap: 12px;
  }
  .brand__dot {
    width: 28px; height: 28px; border-radius: 50%;
    background: var(--brand-blue);
  }
  .brand__rule { width: 1px; height: 52px; background: var(--ink-soft); }
  .brand__name {
    font-weight: 700; font-size: 28px; line-height: 1;
    color: var(--brand-blue); letter-spacing: .5px;
  }
  .brand__sub {
    margin-top: 2px;
    font-weight: 300; font-size: 12px; letter-spacing: 2.6px;
    color: var(--ink-soft);
  }
  .brand__web {
    margin-top: 3px;
    font-weight: 700; font-size: 10px; letter-spacing: 1px;
    color: var(--brand-blue);
  }

  .addresses {
    position: absolute; left: 40px; bottom: 34px;
    list-style: none;
    font-weight: 400; font-size: 11px; color: var(--ink);
  }
  .addresses li { display: flex; align-items: center; gap: 8px; margin-top: 5px; }
  .addresses svg { width: 8px; height: 11px; flex: none; }

  .band-blue {
    position: absolute; left: 0; bottom: 0; width: 64%; height: 12px;
    background: var(--brand-blue);
    box-shadow: 0 -3px 0 var(--band-pale);
  }
  .band-grey {
    position: absolute; right: 0; bottom: 0; width: 36%; height: 12px;
    background: var(--band-grey);
  }
  .band-grey-side {
    position: absolute; right: 0; top: 0; width: 12px; height: 100%;
    background: var(--band-grey);
  }
</style>
</head>
<body>
<main class="canvas">

  <section class="envelope envelope--back" aria-label="Envelope back">
    <div class="envelope__flap"><span class="envelope__flap-mark"></span></div>
  </section>

  <section class="envelope envelope--front" aria-label="Envelope front">
    <div class="brand">
      <span class="brand__dot"></span>
      <span class="brand__rule"></span>
      <div>
        <div class="brand__name">SUMMIT</div>
        <div class="brand__sub">ENDODONTICS</div>
        <div class="brand__web">SUMMITENDO.COM</div>
      </div>
    </div>

    <ul class="addresses">
      <li>
        <svg viewBox="0 0 8 11"><path d="M4 0a4 4 0 0 0-4 4c0 3 4 7 4 7s4-4 4-7a4 4 0 0 0-4-4zm0 5.5A1.5 1.5 0 1 1 4 2.5a1.5 1.5 0 0 1 0 3z" fill="#1f5fb0"/></svg>
        842 Laurel Street, Riverton, CA 95820
      </li>
      <li>
        <svg viewBox="0 0 8 11"><path d="M4 0a4 4 0 0 0-4 4c0 3 4 7 4 7s4-4 4-7a4 4 0 0 0-4-4zm0 5.5A1.5 1.5 0 1 1 4 2.5a1.5 1.5 0 0 1 0 3z" fill="#1f5fb0"/></svg>
        3150 Oak Grove Ave. Suite #4, Fairview, CA 95612
      </li>
    </ul>

    <div class="band-grey-side"></div>
    <div class="band-blue"></div>
    <div class="band-grey"></div>
  </section>

</main>
</body>
</html>
```